lantern institute of business and technology web site

I need web site for the institute which focus on business courses and computer course it is also for vocation train for employment It is also carear development and advancement .It should have links to online study resource which free
Industry/Entity Type
Business
Number of Pages Required
1 page
Look and feel

```html
<!DOCTYPE html>
<html lang="en">
<head>
<meta charset="utf-8">
<title>Lantern Institute of Business and Technology</title>
<link href="https://fonts.googleapis.com/css2?family=Open+Sans:wght@400;600;700&family=Roboto+Condensed:wght@400;700&display=swap" rel="stylesheet">
<style>
:root{
  --navy:#1f2a5c;
  --navy-deep:#18214a;
  --blue:#1a9be0;
  --green:#58a23a;
  --orange:#f29a26;
  --charcoal:#3a3a3c;
  --ink:#2a2a2a;
  --muted:#6d6d6d;
  --link:#2a4fa0;
  --white:#ffffff;
  --pale:#eef0f4;
}
*{box-sizing:border-box;margin:0;padding:0}
html,body{width:1200px;height:2540px;overflow:hidden}
body{font-family:"Open Sans",Arial,sans-serif;color:var(--ink);background:var(--white);position:relative}
.head{font-family:"Roboto Condensed","Arial Narrow",sans-serif;font-weight:700;text-transform:uppercase}
ul{list-style:none}

/* hero */
.hero{position:absolute;left:0;top:0;width:1200px;height:580px;
  background:linear-gradient(180deg,#5a4536 0%,#8a6a52 35%,#b08e74 60%,#6b5b55 100%)}
.topbar{position:absolute;left:0;top:0;width:1200px;height:64px;background:rgba(24,33,74,.88);display:flex;align-items:center;justify-content:space-between;padding:0 50px}
.brand{display:flex;align-items:center;gap:12px;color:var(--white)}
.brand-mark{width:34px;height:34px;background:var(--white)}
.brand-name{font-family:"Roboto Condensed",sans-serif;font-weight:700;font-size:17px;line-height:18px;text-transform:uppercase}
.nav{display:flex;gap:22px}
.nav a{color:var(--white);text-decoration:none;font-size:12px;font-weight:600;text-transform:uppercase}

/* top courses band */
.courses-band{position:absolute;left:0;top:580px;width:1200px;height:220px;background:var(--navy);color:var(--white);padding:30px 60px}
.courses-band h2{font-size:30px;line-height:32px;width:360px}
.rule{width:60px;height:3px;background:var(--blue);margin:12px 0 20px}
.helpdesk{display:flex;align-items:center;gap:14px;font-size:12px;font-weight:700;text-transform:uppercase}
.helpdesk .nums{border-left:1px solid rgba(255,255,255,.4);padding-left:14px;font-size:14px;line-height:18px}
.course-col{position:absolute;top:30px;font-size:11px;line-height:17px}
.course-col h3{font-size:13px;margin-bottom:6px}
.course-col h3+ul+h3{margin-top:12px}
.course-col li{opacity:.85}
.view-all{display:inline-block;margin-top:14px;font-size:13px;font-weight:700;color:var(--white)}

/* popular courses */
.popular{position:absolute;left:0;top:800px;width:1200px;height:540px;padding:60px 60px}
.popular h2{font-size:30px;line-height:32px;color:var(--ink)}
.popular .rule{background:var(--navy)}
.popular p{width:560px;font-size:12px;line-height:18px;color:var(--muted)}
.popular h4{margin:26px 0 12px;font-size:14px;color:var(--navy)}
.program-list{display:grid;grid-template-columns:260px 260px;row-gap:8px;font-size:12px}
.program-list li{color:var(--link)}
.program-list li::before{content:"›";margin-right:8px;color:var(--blue);font-weight:700}
.tiles{position:absolute;left:700px;top:50px;display:grid;grid-template-columns:240px 240px;grid-template-rows:170px 170px}
.tile{color:var(--white);text-align:center;padding:26px 20px;font-size:11px;line-height:15px}
.tile h5{font-size:13px;margin:10px 0 6px}
.tile svg{display:block;margin:0 auto}
.t-blue{background:var(--blue)}.t-green{background:var(--green)}.t-navy{background:var(--navy)}.t-orange{background:var(--orange)}

/* highlights */
.highlights{position:absolute;left:0;top:1340px;width:1200px;height:700px;background:var(--charcoal)}
.hl-title{position:absolute;left:60px;top:32px;width:1080px;height:44px;background:var(--white);display:flex;align-items:center;justify-content:center;font-size:20px;color:var(--ink);letter-spacing:.5px}
.hl-grid{position:absolute;left:60px;top:96px;display:grid;grid-template-columns:360px 360px 360px;grid-template-rows:290px 290px}
.hl-card{color:var(--white);text-align:center;padding:22px 26px;font-size:12px;line-height:18px}
.hl-card h5{background:var(--white);display:inline-block;padding:8px 30px;font-size:16px;margin-bottom:18px}
.c-blue h5{color:var(--blue)}.c-orange h5{color:var(--orange)}.c-green h5{color:var(--green)}
.c-blue{background:var(--blue)}.c-orange{background:var(--orange)}.c-green{background:var(--green)}
.more{display:block;margin-top:18px;font-size:11px;font-weight:700;text-transform:uppercase}
.ph-grads{background:linear-gradient(160deg,#cfd4d8,#8a8f95 50%,#2b2b30)}
.ph-library{background:linear-gradient(160deg,#7b5a3a,#b48b5d 50%,#4a3a2c)}
.ph-student{background:linear-gradient(160deg,#a7c98a,#d9c3a3 50%,#6f8f55)}

/* partners */
.partners{position:absolute;left:0;top:2040px;width:1200px;height:140px;display:flex;align-items:center;justify-content:space-between;padding:0 80px}
.badge{width:150px;height:40px;background:#bcbcbc}

/* footer */
.footer{position:absolute;left:0;top:2180px;width:1200px;height:300px;background:var(--navy);color:var(--white);padding:34px 60px}
.foot-brand{position:absolute;left:60px;top:50px;width:220px}
.foot-brand .mark{width:120px;height:110px;background:#3a4678;margin-bottom:14px}
.foot-brand .name{font-family:"Roboto Condensed",sans-serif;font-weight:700;font-size:15px;line-height:18px;text-transform:uppercase}
.foot-col{position:absolute;top:34px;font-size:11px;line-height:20px}
.foot-col h6{font-size:13px;margin-bottom:8px}
.foot-col li{opacity:.8}
.social li{display:flex;align-items:center;gap:8px}
.social li::before{content:"";width:12px;height:12px;background:var(--blue)}
.bottom{position:absolute;left:0;top:2480px;width:1200px;height:60px;background:var(--navy-deep);color:rgba(255,255,255,.7);font-size:10px;padding:16px 60px;line-height:14px}
</style>
</head>
<body>

<header class="hero" role="img" aria-label="Photograph of smiling students with books in a library">
  <div class="topbar">
    <div class="brand"><span class="brand-mark"></span><span class="brand-name">Lantern Institute<br>of Business &amp; Technology</span></div>
    <nav class="nav"><a href="#">Home</a><a href="#">About Us</a><a href="#">Courses</a><a href="#">Apply Online</a><a href="#">Help Desk</a><a href="#">Contact</a></nav>
  </div>
</header>

<section class="courses-band">
  <h2 class="head">Our Top IT and Business Courses</h2>
  <div class="rule"></div>
  <div class="helpdesk">
    <svg width="26" height="26" viewBox="0 0 24 24"><path fill="#fff" d="M6.6 10.8a15 15 0 0 0 6.6 6.6l2.2-2.2a1 1 0 0 1 1-.25 11.4 11.4 0 0 0 3.6.57 1 1 0 0 1 1 1V20a1 1 0 0 1-1 1A17 17 0 0 1 3 4a1 1 0 0 1 1-1h3.5a1 1 0 0 1 1 1c0 1.25.2 2.45.57 3.6a1 1 0 0 1-.25 1z"/></svg>
    <span>Office<br>Helpdesk</span>
    <span class="nums">555-210-4400<br>555-210-4411</span>
  </div>
  <div class="course-col" style="left:500px">
    <h3 class="head">Undergraduate</h3>
    <ul><li>Bachelor of Science in Information Technology (BSc IT)</li><li>Bachelor of Computer Applications (BCA)</li><li>Bachelor of Business Administration (BBA)</li><li>Bachelor of Commerce (BCom)</li></ul>
    <h3 class="head">Certificate Level Programs 1 Year</h3>
    <ul><li>Information Security</li><li>Cloud Computing</li><li>Mobile Application &amp; Technology</li></ul>
  </div>
  <div class="course-col" style="left:860px">
    <h3 class="head">Post Graduate &amp; Diploma</h3>
    <ul><li>Master of Computer Application (MCA)</li><li>Master of Science in Information Technology (MSc IT)</li><li>Master of Business Administration (MBA)</li></ul>
    <h3 class="head">Post Graduate Diploma</h3>
    <ul><li>PG Diploma in Computer Applications (PGDCA)</li><li>PG Diploma in Information Technology (PGDIT)</li></ul>
    <a class="view-all head" href="#">View All Courses</a>
  </div>
</section>

<section class="popular">
  <h2 class="head">Our Popular IT<br>and Business Courses</h2>
  <div class="rule"></div>
  <p>Build practical skills for employment and career advancement with our business and computer programmes. Flexible schedules, hands-on training and free online study resources help every learner move forward with confidence.</p>
  <h4 class="head">Popular Programs &amp; Courses</h4>
  <ul class="program-list">
    <li>Under Graduate Programs</li><li>Diploma Programs</li>
    <li>Master Degree Programs</li><li>Advanced Diploma Programs</li>
    <li>Post Graduate Programs</li><li>Finance &amp; Accounting Courses</li>
    <li>Certificate Level Programs</li><li>Website Information Technology</li>
  </ul>
  <div class="tiles">
    <div class="tile t-blue">
      <svg width="40" height="40" viewBox="0 0 40 40"><path fill="#fff" d="M20 6 2 15l18 9 18-9zM9 20v8c0 3 5 6 11 6s11-3 11-6v-8l-11 6z"/></svg>
      <h5 class="head">Business Course</h5>Career-focused courses in management, accounts and trade.
    </div>
    <div class="tile t-green">
      <svg width="40" height="40" viewBox="0 0 40 40"><rect x="5" y="8" width="30" height="20" fill="none" stroke="#fff" stroke-width="3"/><rect x="14" y="30" width="12" height="3" fill="#fff"/></svg>
      <h5 class="head">IT Course</h5>Computer skills from basics to software development.
    </div>
    <div class="tile t-navy">
      <svg width="40" height="40" viewBox="0 0 40 40"><circle cx="20" cy="20" r="14" fill="none" stroke="#fff" stroke-width="3"/><circle cx="20" cy="20" r="7" fill="none" stroke="#fff" stroke-width="3"/><circle cx="20" cy="20" r="2" fill="#fff"/></svg>
      <h5 class="head">Vocation Learning</h5>Job-ready vocational training for direct employment.
    </div>
    <div class="tile t-orange">
      <svg width="40" height="40" viewBox="0 0 24 24"><path fill="#fff" d="M6.6 10.8a15 15 0 0 0 6.6 6.6l2.2-2.2a1 1 0 0 1 1-.25 11.4 11.4 0 0 0 3.6.57 1 1 0 0 1 1 1V20a1 1 0 0 1-1 1A17 17 0 0 1 3 4a1 1 0 0 1 1-1h3.5a1 1 0 0 1 1 1c0 1.25.2 2.45.57 3.6a1 1 0 0 1-.25 1z"/></svg>
      <h5 class="head">Technical Support</h5>Friendly guidance for study and free online resources.
    </div>
  </div>
</section>

<section class="highlights">
  <div class="hl-title head">Our Program Highlights and Innovative Technologies</div>
  <div class="hl-grid">
    <div class="hl-card c-blue"><h5 class="head">Excellent Training</h5><p>Learn from experienced trainers in modern classrooms with practical projects that prepare you for real workplaces.</p><span class="more">Click here to know more</span></div>
    <div class="ph-grads" role="img" aria-label="Photograph of graduates in caps and gowns"></div>
    <div class="hl-card c-orange"><h5 class="head">Anytime Anywhere</h5><p>Study at your own pace with free online resources, recorded lessons and guided support whenever you need it.</p><span class="more">Click here to know more</span></div>
    <div class="ph-library" role="img" aria-label="Photograph of a student reading in a library"></div>
    <div class="hl-card c-green"><h5 class="head">Digital Technology</h5><p>Get hands-on with current software, networks and digital tools used across business and industry today.</p><span class="more">Click here to know more</span></div>
    <div class="ph-student" role="img" aria-label="Photograph of a smiling student holding books outdoors"></div>
  </div>
</section>

<section class="partners" aria-label="Partner institutions">
  <div class="badge"></div><div class="badge"></div><div class="badge"></div><div class="badge"></div><div class="badge"></div>
</section>

<footer class="footer">
  <div class="foot-brand"><div class="mark"></div><div class="name">Lantern Institute of<br>Business &amp; Technology</div></div>
  <div class="foot-col" style="left:440px"><h6 class="head">Quick Links</h6><ul><li>Home</li><li>About Us</li><li>Courses</li><li>Apply Online</li><li>Help Desk</li><li>Contact Us</li></ul></div>
  <div class="foot-col" style="left:620px"><h6 class="head">Academics</h6><ul><li>Course Application Forms</li><li>Exam Dates</li><li>Application Deadline</li><li>Study Materials</li><li>Faculty</li><li>Board / Exchange</li></ul></div>
  <div class="foot-col" style="left:820px"><h6 class="head">Campus</h6><ul><li>Campus Information</li><li>Digital Library</li><li>Terms &amp; Conditions</li><li>Students Area</li><li>Apply Now</li><li>Downloads</li></ul></div>
  <div class="foot-col social" style="left:1000px"><h6 class="head">Get Connected</h6><ul><li>Community Page</li><li>News Feed</li><li>Circle Updates</li><li>Video Channel</li></ul></div>
</footer>
<div class="bottom">Copyright 2024. All rights reserved.<br>Terms &amp; Conditions &nbsp;|&nbsp; Privacy &nbsp;|&nbsp; Disclaimer</div>

</body>
</html>
```